Professional book cover needed for an ethical influence training company

We need a professional/sharp book cover for our new book, "Reach to Harvest"

This book teaches business owners, marketers, sales professionals and leaders how to better their communication with their customers and team.

Our company teaches home study courses and also live events around the topic, and this book will be the first impression and representation of us to new potential clients.

We are undecided if we should use my face on the cover or not, we are open to ideas and suggestions

To see other books in a similar category, you can look at the business/money category on Corvane: https://www.corvane-shop.example/s/ref=lp_000000_nr_n_2?fst=as%3Aoff&rh=n%3A000000%2Cn%3A%210000%2Cn%3A3&bbn=0000&ie=UTF8&qid=0000000000&rnid=0000

Target Market(s)

Small business owners, marketers, sales people

Industry/Entity Type

Business

Font styles to use
Sans Serif

Requirements
Must have
• A professional, sharp feel.
• Colors to match the logo attached (which one of your designers created, thank you!)
• Website: www.ReachToHarvest.example (this new book will most likely replace the book featured on the website)
• Please do not use the logo on the book though.
• We will need the book cover to be fully editable when the file is delivered, as well as the names of any fonts used.
• Number of Pages 100
• Book Size: 6 x 9
• Bleed Dimensions: 12.4752 x 9.25
• Trim Guides Horizontal: 0.125 and 12.3502
• Trim Guides Vertical: 0.125 and 9.125
• Safe Zone Guides Horizontal: 0.25 and 12.2252
• Safe Zone Guides Vertical: 0.25 and 9
• Spine Dimensions: 0.2252
• Spine Guides: 6.125 and 6.3502
• PDF template attached for reference
Nice to have
• We are undecided if we would like to use my face on the front book cover or not. It should be at least on the back page if not on the front.
Should not have
• Please do not use the logo on the book cover, but we would like the feel to match.
• Nothing that looks "cute" it is not a children's book
• Nothing that looks "soft" or feminine.

```html
<!DOCTYPE html>
<html lang="en">
<head>
<meta charset="utf-8">
<title>Reach to Harvest – Book Cover</title>
<link href="https://fonts.googleapis.com/css2?family=Oswald:wght@400;500&family=Arimo&display=swap" rel="stylesheet">
<style>
  :root {
    --green-top: #49b04b;
    --green-bottom: #2b7b3b;
    --blue-top: #2356a8;
    --blue-bottom: #101a48;
    --white: #ffffff;
    --photo-warm: #b79a86;
    --photo-cool: #c9c6d0;
  }
  html, body { margin: 0; padding: 0; overflow: hidden; }
  body { width: 1200px; height: 890px; }
  .cover {
    position: relative;
    width: 1200px; height: 890px; overflow: hidden;
    background: linear-gradient(180deg, var(--green-top) 0%, var(--green-bottom) 100%);
    font-family: "Arimo", Arial, sans-serif;
    color: var(--white);
  }
  .artwork { position: absolute; inset: 0; }
  .title-text { font-family: "Oswald", sans-serif; font-weight: 500; fill: var(--white); }
  .back-copy {
    position: absolute; left: 54px; width: 494px;
    font-size: 14.6px; line-height: 19.2px; text-align: justify; hyphens: auto; margin: 0;
  }
  .back-copy.first { top: 284px; }
  .back-copy.second { top: 440px; }
  .author-photo {
    position: absolute; left: 57px; top: 547px; width: 117px; height: 147px;
    background: linear-gradient(180deg, #d9e3ea 0%, var(--photo-warm) 45%, var(--photo-cool) 100%);
  }
  .author-bio {
    position: absolute; left: 185px; top: 589px; width: 363px; margin: 0;
    font-size: 14.6px; line-height: 19.4px; text-align: justify; hyphens: auto;
  }
  .brand-plate {
    position: absolute; left: 64px; top: 804px; width: 178px; height: 36px;
    background: var(--white); display: flex; align-items: center; justify-content: center;
    color: var(--blue-top); font-family: "Oswald", sans-serif; font-weight: 500; font-size: 16px;
  }
  .code-box { position: absolute; left: 385px; top: 745px; width: 163px; height: 101px; background: var(--white); }
  .author-portrait {
    position: absolute; left: 912px; top: 476px; width: 288px; height: 414px;
    background: radial-gradient(ellipse at 55% 30%, var(--photo-warm) 0%, #8c6f60 40%, var(--photo-cool) 70%, #9e98a8 100%);
    border-radius: 140px 140px 0 0;
  }
</style>
</head>
<body>
<main class="cover">
  <svg class="artwork" width="1200" height="890" viewBox="0 0 1200 890" role="presentation">
    <defs>
      <linearGradient id="chartFill" x1="0" y1="0" x2="0" y2="1">
        <stop offset="0" stop-color="#2356a8"/>
        <stop offset="1" stop-color="#101a48"/>
      </linearGradient>
    </defs>
    <polygon class="chart-area" fill="url(#chartFill)"
      points="128,890 832,670 940,516 1036,572 1200,300 1200,890"/>
    <polyline class="chart-line" fill="none" stroke="#fff" stroke-width="12" stroke-linejoin="round"
      points="150,893 832,670 940,516 1036,572 1170,336"/>
    <polygon class="chart-arrowhead" fill="#fff" points="1190,303 1118,345 1192,382"/>
    <circle cx="832" cy="670" r="19" fill="#fff"/>
    <circle cx="940" cy="516" r="19" fill="#fff"/>

    <g class="back-title">
      <text class="title-text" x="166" y="102" font-size="74" textLength="270" lengthAdjust="spacingAndGlyphs">REACH</text>
      <line x1="170" y1="125" x2="280" y2="125" stroke="#fff" stroke-width="1.5"/>
      <line x1="324" y1="125" x2="434" y2="125" stroke="#fff" stroke-width="1.5"/>
      <text class="title-text" x="302" y="140" font-size="36" text-anchor="middle">TO</text>
      <text class="title-text" x="166" y="238" font-size="111" textLength="268" lengthAdjust="spacingAndGlyphs">HARVEST</text>
    </g>

    <g class="front-title">
      <text class="title-text" x="684" y="140" font-size="116" textLength="434" lengthAdjust="spacingAndGlyphs">REACH</text>
      <line x1="688" y1="179" x2="870" y2="179" stroke="#fff" stroke-width="1.5"/>
      <line x1="942" y1="179" x2="1118" y2="179" stroke="#fff" stroke-width="1.5"/>
      <text class="title-text" x="906" y="204" font-size="56" text-anchor="middle">TO</text>
      <text class="title-text" x="688" y="364" font-size="172" textLength="430" lengthAdjust="spacingAndGlyphs">HARVEST</text>
    </g>

    <g class="front-subtitle" font-family="Oswald, sans-serif" font-weight="400" font-size="25" fill="#fff" letter-spacing="1.2" text-anchor="middle">
      <text x="902" y="420">GROWING YOUR BUSINESS THROUGH</text>
      <text x="902" y="451">HONEST AND CLEAR COMMUNICATION</text>
    </g>

    <text class="title-text author-name-back" x="184" y="578" font-size="37">DANIEL MARSH</text>
    <text class="title-text author-name-front" x="632" y="832" font-size="40">DANIEL MARSH</text>
  </svg>

  <p class="back-copy first">Lorem ipsum dolor sit amet, consectetur adipiscing elit. In sollicitudin vulputate lacinia. Praesent ultrices dictum auctor. Mauris dictum volutpat velit ut maximus. Aenean consectetur hendrerit dolor vel egestas. Phasellus consequat dictum congue. Nunc a ante augue. Maecenas sed ipsum et nibh interdum egestas eu placerat ipsum. Suspendisse viverra convallis efficitur. Mauris posuere pretium velit. Vivamus rhoncus dictum turpis, a ornare ex vulputate ut.</p>
  <p class="back-copy second">Lorem ipsum dolor sit amet, consectetur adipiscing elit. In sollicitudin vulputate lacinia. Praesent ultrices dictum auctor. Mauris dictum volutpat velit ut maximus. Aenean consectetur hendrerit dolor vel egestas. Phasellus consequat dictum congue.</p>

  <div class="author-photo" role="img" aria-label="Author photo: smiling man in striped shirt by the sea"></div>
  <p class="author-bio">Lorem ipsum dolor sit amet, consectetur adipiscing elit. In sollicitudin vulputate lacinia. Praesent ultrices dictum auctor. Mauris dictum volutpat velit ut maximus. Aenean consectetur hendrerit dolor vel egestas. Phasellus consequat dictum congue.</p>

  <div class="brand-plate">ReachToHarvest.example</div>
  <div class="code-box"></div>

  <div class="author-portrait" role="img" aria-label="Author portrait: smiling man in a striped shirt"></div>
</main>
</body>
</html>
```